LUSTRIA INC. is a new Fashion Stylist, Design Merchandiser, and consultant in the fashion industry

We need a logo design for a new Calgary, Alberta based company that is in the business of making over your image, wardrobe and style for both business and personal purposes.

Target Market(s)

Professional female and male business people looking for a new style or complete fashion makeover including clothes closet merchandising and makeover.

Contact Information for Business Card

Number of Pages Required

1 page

Font styles to use
Script

Colors
fac994
fbe7d2
fee3d4

Requirements
Must have
• Fashion Industry theme that is very elegant and colorful using gold/bronze/silver color themes.
Nice to have
• Incorporate the company name with the creative font to come up with the appropriate "logo"

```html
<!DOCTYPE html>
<html lang="en">
<head>
<meta charset="utf-8">
<title>LUSTRIA INC. – Business Card</title>
<link rel="stylesheet" href="https://fonts.googleapis.com/css2?family=Kaushan+Script&display=swap">
<style>
  :root {
    --backdrop: #a7a8ac;
    --card-cream: #fae7d3;
    --mark-grey: #58585a;
    --ink: #111111;
    --script: "Kaushan Script", cursive;
  }
  html, body {
    margin: 0;
    padding: 0;
    width: 1200px;
    height: 942px;
    overflow: hidden;
    background: var(--backdrop);
  }
  .canvas {
    position: relative;
    width: 1200px;
    height: 942px;
  }
  .card {
    position: absolute;
    left: 256px;
    width: 674px;
    height: 385px;
    background: var(--card-cream);
    border-radius: 16px;
    font-family: var(--script);
    text-align: center;
  }
  .card--front { top: 48px; }
  .card--back  { top: 494px; }
  .brand-name {
    position: absolute;
    left: 0;
    right: 0;
    margin: 0;
    color: var(--mark-grey);
    font-weight: 400;
    font-size: 54px;
    line-height: 1;
  }
  .card--front .brand-name { top: 52px; }
  .card--back .brand-name { top: 160px; }
  .person-name {
    position: absolute;
    left: 0; right: 0;
    top: 180px;
    margin: 0;
    color: var(--ink);
    font-size: 27px;
    font-weight: 400;
    letter-spacing: 0.5px;
    line-height: 1;
  }
  .services {
    position: absolute;
    left: 0; right: 0;
    top: 230px;
    margin: 0;
    color: var(--ink);
    font-size: 15px;
    letter-spacing: 1.2px;
    line-height: 1;
  }
  .phone {
    position: absolute;
    left: 0; right: 0;
    top: 270px;
    margin: 0;
    color: var(--ink);
    font-size: 13px;
    letter-spacing: 0.8px;
    line-height: 1;
  }
</style>
</head>
<body>
<main class="canvas">
  <section class="card card--front">
    <p class="brand-name">LUSTRIA INC.</p>
    <h1 class="person-name">MARIKA VAN HOLTEREN</h1>
    <p class="services">fashion stylist design merchandiser consultant</p>
    <p class="phone">403-555-0142</p>
  </section>
  <section class="card card--back">
    <p class="brand-name">LUSTRIA INC.</p>
  </section>
</main>
</body>
</html>
```